Website redesign for a Cloud Advisory business

We are looking to revisit our existing brand and website, with a view to updating both. Looking for concepts and designs for how the website might look, flow and feel. Current website is: www.brellomint.com.au

Scope and Deliverables: Concept design for the home page and one internal page.

We do not expect you to design all the pages and all the elements of the website at this stage.

This job is not for the full website design, but just for concepts that we can start with when we go into the full website design.

We would love to see a design feature based on our name, logo, or industry, which can run through banners and other collateral (twitter banner, ads on Google, corporate documents etc).

We want the brand to properly depict what we bring/deliver to businesses when consulting to them and this should extend to the colour scheme, logo, font (perhaps updated) and copy (which will be supplied).

Our brand should suitably communicate our ability, knowledge and extensive experience within the Cloud space.

It should express and evoke credibility, knowledge and understanding of the Cloud space, independence, gravitas, reliability, efficiency, trust, expertise, approachability, service delivery but be uncomplicated, practical and use plain speaking language.

Colours that reinforce this might include: Blues, blacks, silver, white, grey and our existing orange.

Website designs that we like or have referenced include:

Varnolift: http://varnolift.com.au/ - This has good information but looks a little amateur in it’s cartoon like design and colour scheme. Also, this seems to be aimed at clients more interested in price than design and what we are going for is a little more high end.

Pendramoor: https://www.pendramoor.com.au/ - This site has merit in its’ setup but little call to action on the home page, especially before the scroll line. I like the set up of the Case Studies page however I’d look to make it more prominent by having it set up 3 across rather than the 4 they have. Something such as this: https://www.qandelby.com/case-studies

Tolvane: http://www.tolvane.com.au/#home4 - This page is a good one as far as selling services and information on the company. I quite like it.

MirefoldIT: http://www.mirefoldit.com.au/ - While I don’t think is particularly creative, it does practically depict the services we offer in a fairly clear way and might be a bit of a basic (albeit dull) template to follow.

JDP: https://store.jdp.com/us/Product-Family/JDP-Advisory-Services/JDP-Cloud-Advisory-Service/p/JDP-Services-Cloud-Advisory - This offers substantial information but is probably a little confusing although the roll-over drop down menus have merit.

ZEV: http://www.zev.net.au/en/services/ - While this in not quite what we are looking for, the colour scheme gives it more gravitas and quality.

As another reference, this website and the way they present their case studies is also something we like, although I’d like them shown 3 up, side by side…. https://www.qandelby.com/case-studies.

We have added a page layout and page purpose document.

Target Market(s)

Corporates, small - medium business, direct referrals, via search results

Industry/Entity Type

Business

Number of Pages Required

1 page

Font styles to use
Sans Serif

Colors
85abd2
0455a3
000000
f37122
5c5c5c

Requirements
Must have
• Website must be mobile device compatible.
• Concept design for the home page.
Nice to have
• We would love to see a design feature based on our name, logo, or industry, which can run through banners and other collateral (twitter banner, ads on Google, corporate documents etc).

```html
<!DOCTYPE html>
<html lang="en">
<head>
<meta charset="utf-8">
<title>Brellomint – Impartial Cloud Solutions</title>
<link href="https://fonts.googleapis.com/css2?family=Open+Sans:ital,wght@0,400;0,600;0,700;0,800;1,400;1,600&display=swap" rel="stylesheet">
<style>
:root{
  --orange:#f37122;
  --orange-dark:#d95d12;
  --blue:#0455a3;
  --blue-light:#85abd2;
  --ink:#1c1c1c;
  --grey:#5c5c5c;
  --grey-light:#8a8a8a;
  --panel:#f1f1f1;
  --line:#dddddd;
  --nav:#1d1d1d;
  --footer:#1f1f1f;
  --white:#ffffff;
}
*{margin:0;padding:0;box-sizing:border-box}
html,body{width:1200px;height:2708px;overflow:hidden}
body{font-family:"Open Sans",Arial,sans-serif;color:var(--grey);background:var(--white);position:relative}
section,header,nav,footer,.copyright{position:absolute;left:0;width:1200px}

/* top navigation */
.main-nav{top:0;height:36px;background:var(--nav);display:flex;justify-content:center}
.main-nav a{color:#e6e6e6;font-size:11px;font-weight:600;letter-spacing:.6px;text-decoration:none;padding:0 22px;line-height:36px;text-transform:uppercase}
.main-nav a.active{background:var(--orange);color:var(--white)}

/* header */
.site-header{top:36px;height:84px;display:flex;align-items:center;justify-content:space-between;padding:0 80px;background:var(--white)}
.brand{display:flex;align-items:center;gap:10px}
.brand-mark{width:26px;height:26px;background:var(--orange)}
.brand-name{font-size:30px;font-weight:800;color:var(--ink);letter-spacing:1px}
.header-tools{display:flex;align-items:center;gap:8px}
.search{width:150px;height:26px;border:1px solid var(--line);font-size:11px;color:var(--grey-light);padding:0 8px;line-height:24px}
.social-dot{width:24px;height:24px;border-radius:50%;background:var(--ink)}

/* hero */
.hero{top:120px;height:580px;background:linear-gradient(180deg,#4a4d52 0%,#2a2c30 55%,#1b1c1f 100%);text-align:center;color:var(--white)}
.hero-photo{position:absolute;inset:0;background:radial-gradient(ellipse at 70% 40%,rgba(140,150,160,.35),transparent 60%)}
.hero-content{position:absolute;top:230px;left:0;width:100%}
.hero h1{font-size:44px;font-weight:600;letter-spacing:3px}
.hero h1 span{color:var(--orange)}
.hero-band{display:inline-block;background:var(--orange);font-size:19px;font-weight:600;letter-spacing:1.5px;padding:4px 18px;margin-top:12px}
.hero-sub{font-size:19px;font-weight:600;letter-spacing:1.5px;margin-top:12px}
.hero-actions{margin-top:26px;display:flex;justify-content:center;gap:14px}
.btn{display:inline-block;font-size:12px;font-weight:600;letter-spacing:1px;padding:10px 26px;text-transform:uppercase;color:var(--white)}
.btn-outline{border:1px solid var(--white)}
.btn-orange{background:var(--orange)}
.btn-dark{background:var(--ink);font-size:10px;padding:6px 14px;text-transform:none}

/* solutions */
.solutions{top:700px;height:780px;background:var(--panel);text-align:center}
.section-title{font-size:17px;font-weight:700;letter-spacing:1.5px;color:var(--ink);padding-top:126px}
.section-title span{color:var(--orange)}
.title-rule{width:50px;height:2px;background:var(--orange);margin:10px auto 0}
.solutions-intro{width:720px;margin:24px auto 0;font-size:15px;font-weight:600;line-height:1.6;color:var(--grey)}
.cards{position:absolute;top:348px;left:106px;display:flex;gap:44px}
.card{width:300px;height:272px;background:var(--white);border-top:4px solid var(--orange);box-shadow:0 2px 6px rgba(0,0,0,.12);padding:26px 24px 0}
.card-icon{width:62px;height:62px;margin:0 auto}
.card h3{font-size:13px;font-weight:700;color:var(--ink);margin-top:14px;text-transform:uppercase;letter-spacing:.5px}
.card p{font-size:11px;line-height:1.5;margin:8px 0 12px}
.view-all{position:absolute;top:692px;left:540px;width:120px;text-align:center}

/* welcome & blog */
.welcome{top:1480px;height:420px;background:linear-gradient(120deg,#2b2b2b 0%,#3b3b3b 45%,#242424 100%);color:#d8d8d8}
.welcome-col{position:absolute;top:104px}
.welcome-about{left:80px;width:460px}
.welcome-blog{left:640px;width:480px}
.welcome h2{font-size:16px;font-weight:700;color:var(--white);letter-spacing:1px;text-transform:uppercase}
.welcome .title-rule{margin:8px 0 16px}
.welcome p{font-size:12px;line-height:1.6;margin-bottom:12px}
.blog-item{display:flex;gap:16px;margin-bottom:16px}
.blog-thumb{width:140px;height:80px;flex:none;background:linear-gradient(135deg,#d9d9d9,#8e8e8e)}
.blog-item h4{font-size:12px;font-weight:700;color:var(--orange);text-transform:uppercase}
.blog-item p{font-size:11px;margin:4px 0 0}
.blog-more{font-size:11px;font-weight:700;color:var(--white);text-transform:uppercase;border-bottom:1px solid var(--white)}

/* testimonials */
.testimonials{top:1900px;height:400px;background:var(--white);text-align:center}
.testimonials .section-title{padding-top:48px}
.testimonial{position:absolute;top:140px;left:110px;width:1000px;display:flex;gap:50px;text-align:left}
.client-brand{width:220px;display:flex;gap:10px;align-items:flex-start}
.client-dot{width:26px;height:26px;border-radius:50%;background:var(--blue-light);flex:none}
.client-name{font-size:16px;font-weight:600;color:var(--blue);line-height:1.25}
.client-tag{font-size:10px;color:var(--grey-light);margin-top:6px}
.quote{width:720px;font-size:17px;font-style:italic;line-height:1.5;color:var(--grey);border-left:3px solid var(--line);padding-left:24px}
.quote-author{display:block;margin-top:4px;color:var(--orange);font-weight:600}

/* footer */
.site-footer{top:2300px;height:368px;background:var(--footer);color:#cfcfcf;font-size:11px}
.footer-col{position:absolute;top:54px}
.footer-col h5{font-size:13px;font-weight:700;color:var(--white);letter-spacing:1px;text-transform:uppercase;margin-bottom:16px}
.quicklinks{left:80px;width:300px}
.link-grid{display:grid;grid-template-columns:130px 130px;row-gap:8px}
.useful{left:470px;width:260px;line-height:1.9}
.useful .contact{margin-top:14px}
.message{left:830px;width:290px}
.field-row{display:flex;gap:8px}
.field{background:var(--white);height:24px;flex:1;color:var(--grey-light);font-size:10px;padding:5px 6px}
.field-area{height:86px;margin-top:8px}
.message .btn{margin-top:10px;float:right;font-size:10px;padding:7px 16px}
.copyright{top:2668px;height:40px;background:var(--orange);display:flex;align-items:center;justify-content:space-between;padding:0 80px;color:var(--white);font-size:11px}
.copyright .socials{display:flex;gap:6px}
.copyright .social-dot{width:20px;height:20px;background:var(--white);opacity:.85}
</style>
</head>
<body>

<nav class="main-nav">
  <a class="active">Home</a><a>About Us</a><a>Industry Specialties</a><a>Solutions</a><a>The Company We Keep</a><a>Case Studies</a><a>FAQ</a><a>Contact Us</a>
</nav>

<header class="site-header">
  <div class="brand"><div class="brand-mark"></div><div class="brand-name">BRELLOMINT</div></div>
  <div class="header-tools">
    <div class="search">Keyword Search</div>
    <div class="social-dot"></div><div class="social-dot"></div><div class="social-dot"></div>
  </div>
</header>

<section class="hero">
  <div class="hero-photo" role="img" aria-label="Dim office photograph of business people working at laptops"></div>
  <div class="hero-content">
    <h1>IMPARTIAL <span>CLOUD</span> SOLUTIONS</h1>
    <div class="hero-band">WE PROVIDE IMPARTIAL ADVICE ON CLOUD SOLUTIONS</div>
    <p class="hero-sub">ENSURING IT'S ALWAYS RIGHT FOR YOU.</p>
    <div class="hero-actions"><span class="btn btn-outline">Solutions</span><span class="btn btn-orange">Contact Us</span></div>
  </div>
</section>

<section class="solutions">
  <h2 class="section-title">OUR <span>SOLUTIONS</span></h2>
  <div class="title-rule"></div>
  <p class="solutions-intro">Lorem ipsum dolor sit amet, consectetur adipiscing elit. Phasellus eget leo leo. Sed adipiscing mi orci, vel ultrices turpis mattis a. Quisque sed eros luctus, euismod ligula et, suscipit dolor. Sed et fermentum erat.</p>
  <div class="cards">
    <article class="card">
      <svg class="card-icon" viewBox="0 0 62 62"><circle cx="31" cy="31" r="31" fill="#f37122"/><circle cx="31" cy="31" r="8" fill="#fff"/><g stroke="#fff" stroke-width="3"><line x1="31" y1="12" x2="31" y2="20"/><line x1="31" y1="42" x2="31" y2="50"/><line x1="12" y1="31" x2="20" y2="31"/><line x1="42" y1="31" x2="50" y2="31"/></g></svg>
      <h3>System Selection</h3>
      <p>Find the right systems for you. Choose a cloud strategy covering Inventory Management, Point of Sale, Job Management, Time &amp; Attendance, CRM.</p>
      <span class="btn btn-dark">Read more</span>
    </article>
    <article class="card">
      <svg class="card-icon" viewBox="0 0 62 62"><circle cx="31" cy="31" r="31" fill="#f37122"/><rect x="20" y="15" width="22" height="32" rx="2" fill="#fff"/><g fill="#f37122"><rect x="23" y="18" width="16" height="6"/><rect x="23" y="28" width="4" height="4"/><rect x="29" y="28" width="4" height="4"/><rect x="35" y="28" width="4" height="4"/><rect x="23" y="35" width="4" height="4"/><rect x="29" y="35" width="4" height="4"/><rect x="35" y="35" width="4" height="9"/></g></svg>
      <h3>Accounting Systems &amp; Conversions</h3>
      <p>Convert your Tallybook, Fundwise, Ledgerly, Sheetmaker, Netbooks, Gridsheet to Cloudbook.</p>
      <span class="btn btn-dark">Read more</span>
    </article>
    <article class="card">
      <svg class="card-icon" viewBox="0 0 62 62"><circle cx="31" cy="31" r="31" fill="#f37122"/><circle cx="26" cy="27" r="9" fill="none" stroke="#fff" stroke-width="5" stroke-dasharray="4 3"/><circle cx="38" cy="38" r="7" fill="none" stroke="#fff" stroke-width="4" stroke-dasharray="3 3"/></svg>
      <h3>Integration</h3>
      <p>Automate repetitive tasks, connect your in-house applications, or build a complete "add-on" to market on the Cloudbook community.</p>
      <span class="btn btn-dark">Read more</span>
    </article>
  </div>
  <span class="btn btn-orange view-all">View All</span>
</section>

<section class="welcome" role="img" aria-label="Dark office photograph behind the welcome and blog area">
  <div class="welcome-col welcome-about">
    <h2>Welcome to Brellomint</h2>
    <div class="title-rule"></div>
    <p>Lorem ipsum dolor sit amet, consectetur adipiscing elit. Phasellus eget leo leo. Sed adipiscing mi orci, vel ultrices turpis mattis a. Quisque sed eros luctus, euismod ligula et, suscipit dolor. Sed et fermentum erat. Suspendisse potenti.</p>
    <p>Curabitur tristique vestibulum bibendum. Quisque eget rutrum felis. Nunc a suscipit sem. Nullam volutpat finibus mi et maximus. Donec ac nibh a justo consectetur porttitor. Pellentesque habitant morbi tristique senectus et netus et malesuada fames ac turpis egestas.</p>
  </div>
  <div class="welcome-col welcome-blog">
    <h2>Latest Blog</h2>
    <div class="title-rule"></div>
    <div class="blog-item">
      <div class="blog-thumb" role="img" aria-label="Photo of a person using a laptop"></div>
      <div><h4>Article Title Goes Here</h4><p>Lorem ipsum dolor sit amet, consectetur adipiscing elit. Phasellus eget leo leo. Sed adipiscing mi orci, vel ultrices turpis.</p></div>
    </div>
    <div class="blog-item">
      <div class="blog-thumb" role="img" aria-label="Photo of a team meeting in an office"></div>
      <div><h4>Article Title Goes Here</h4><p>Lorem ipsum dolor sit amet, consectetur adipiscing elit. Phasellus eget leo leo. Sed adipiscing mi orci, vel ultrices turpis.</p></div>
    </div>
    <span class="blog-more">View all articles</span>
  </div>
</section>

<section class="testimonials">
  <h2 class="section-title">WHAT ARE <span>CLIENTS</span> SAYS</h2>
  <div class="title-rule"></div>
  <div class="testimonial">
    <div class="client-brand">
      <div class="client-dot"></div>
      <div><div class="client-name">Larkfield<br>Women's Health<br>Care</div><div class="client-tag">Care for women and families</div></div>
    </div>
    <blockquote class="quote">"Fearing inevitable change from Ledgerly to Cloudbook I was nicely surprised and made to feel comfortable with something that simply works very well indeed. Corwin is a dependable and knowledgeable person in this minefield of accounting software. Highly recommended." <span class="quote-author">- Daniel Morrow</span></blockquote>
  </div>
</section>

<footer class="site-footer">
  <div class="footer-col quicklinks">
    <h5>Quicklinks</h5>
    <div class="link-grid">
      <span>Link 1</span><span>Link 5</span><span>Link 2</span><span>Link 6</span><span>Link 3</span><span>Link 7</span><span>Link 4</span><span>Link 8</span>
    </div>
  </div>
  <div class="footer-col useful">
    <h5>Useful Information</h5>
    <div>Sitemap</div><div>F.A.Q</div><div>Privacy Policy</div><div>Terms &amp; Conditions</div>
    <div class="contact">Harrowdale, Eastmere<br>1300 555 010<br>info@brellomint.com.au</div>
  </div>
  <div class="footer-col message">
    <h5>Quick Message</h5>
    <div class="field-row"><div class="field">Name</div><div class="field">Email</div></div>
    <div class="field field-area">Message</div>
    <span class="btn btn-orange">Send Message</span>
  </div>
</footer>

<div class="copyright">
  <span>Brellomint Copyright 2016 All rights reserved</span>
  <div class="socials"><div class="social-dot"></div><div class="social-dot"></div><div class="social-dot"></div><div class="social-dot"></div></div>
</div>

</body>
</html>
```